ASSET BASED PROGRAM FLIER

Need flier to market hard money loan products offered HARD MONEY FIX & FLIP PROGRAMS

We offer a variety of loan programs Some program highlights include......

1) No Minimum Credit Score
2) 3-5 Day Close
3) Up to 100% of Purchase & Rehab
4) Rates as Low as 7%
5) Loans Offered Nationwide

Contact us today for more information at (800) 647-2915 x42 or email us at mwelton@brightlanefunding.example NMLS #731856 www.brightlanefunding.example

```html
<!DOCTYPE html>
<html lang="en">
<head>
<meta charset="utf-8">
<title>Hard Money Fix &amp; Flip Programs</title>
<link href="https://fonts.googleapis.com/css2?family=Cinzel:wght@700&family=Roboto:ital,wght@0,400;0,500;0,700;1,400&display=swap" rel="stylesheet">
<style>
:root{
  --blue-deep:#0b5aa6;
  --blue-mid:#0a74c4;
  --blue-sky:#12a6e8;
  --blue-royal:#1a5fb4;
  --gold:#b3a25a;
  --gold-light:#d8c67e;
  --charcoal:#3a3a3c;
  --charcoal-dark:#2e2e30;
  --ink:#1e1e1e;
  --white:#ffffff;
  --backdrop:#e9e9ea;
}
*{margin:0;padding:0;box-sizing:border-box}
html,body{width:1200px;height:1200px;overflow:hidden;background:var(--backdrop)}
.poster{
  position:absolute;left:185px;top:16px;width:856px;height:1205px;
  background:var(--white);transform:scale(0.969);transform-origin:0 0;
  overflow:hidden;font-family:"Roboto",Arial,sans-serif;
}
.header-band{position:absolute;left:0;top:0;width:856px;height:600px}
.brand{
  position:absolute;left:505px;top:112px;width:200px;
  display:flex;align-items:center;gap:8px;justify-content:center;
}
.brand-dot{width:16px;height:16px;border-radius:50%;background:var(--gold);flex:none}
.brand-name{font-family:"Roboto",Arial,sans-serif;font-weight:700;font-size:15px;color:var(--blue-deep);white-space:nowrap}
.hero-photo{
  position:absolute;left:32px;top:177px;width:824px;height:381px;
  background:linear-gradient(100deg,#6b8f5a 0%,#d9d2c8 30%,#efece6 60%,#e3ded6 100%);
}
.headline{position:absolute;left:80px;top:578px;font-family:"Cinzel",serif;font-weight:700;line-height:1}
.headline .line-one{display:block;font-size:62px;color:var(--blue-deep);letter-spacing:1px}
.headline .line-two{display:block;font-size:79px;color:var(--gold);margin-top:4px;letter-spacing:1px}
.about{
  position:absolute;left:80px;top:748px;width:384px;
  font-size:17px;line-height:21px;color:var(--ink);text-align:justify;
}
.gallery{position:absolute;left:0;top:882px;width:470px;height:224px;background:var(--gold)}
.gallery-photo{position:absolute;top:11px;height:178px;border:3px solid #2a2418}
.gallery-photo.before{left:14px;width:204px;background:linear-gradient(160deg,#e8e2d6,#c48a4a 55%,#b9a98e)}
.gallery-photo.after{left:226px;width:222px;background:linear-gradient(160deg,#5a4a3a,#2a1f18 55%,#8a6e4a)}
.gallery-label{position:absolute;top:194px;font-family:"Cinzel",serif;font-weight:700;font-size:17px;color:var(--white);letter-spacing:1px}
.gallery-label.before{left:80px}
.gallery-label.after{left:307px}
.programs{
  position:absolute;left:497px;top:742px;width:359px;height:385px;
  background:linear-gradient(160deg,var(--charcoal-dark),var(--charcoal) 60%,#444446);
  border-top:8px solid var(--gold);
}
.programs-title{position:absolute;left:11px;top:12px;font-size:23px;line-height:28px;color:var(--white);font-weight:400}
.programs-title span{color:var(--gold-light);font-weight:500;display:inline-block;border-bottom:1px solid #9a9a9a;padding-bottom:2px}
.program-list{list-style:none;position:absolute;left:8px;top:100px}
.program-item{position:absolute;left:0;display:flex;align-items:center;gap:16px;width:340px;
  font-weight:700;font-size:17px;line-height:21px;color:var(--white)}
.program-icon{width:38px;height:38px;flex:none}
.footer{
  position:absolute;left:0;top:1127px;width:856px;height:78px;background:var(--blue-deep);
  color:var(--white);font-size:15.5px;line-height:19px;text-align:center;padding-top:5px;
}
.footer .phone{color:var(--gold-light);font-style:italic}
.footer em{font-style:italic}
</style>
</head>
<body>
<div class="poster">
  <svg class="header-band" viewBox="0 0 856 600" aria-hidden="true">
    <rect x="0" y="0" width="856" height="177" fill="var(--blue-deep)"/>
    <polygon points="0,0 560,0 430,120 0,40" fill="#0d62b0"/>
    <polygon points="0,80 360,177 0,177" fill="var(--blue-mid)"/>
    <polygon points="0,177 32,177 32,555 0,588" fill="var(--blue-mid)"/>
    <polygon points="0,230 32,177 32,420 0,520" fill="var(--blue-sky)" opacity=".55"/>
    <polygon points="640,0 856,0 856,40 740,60" fill="var(--blue-royal)"/>
    <polygon points="740,60 856,0 856,177" fill="var(--blue-sky)"/>
    <polygon points="700,0 760,0 740,60" fill="#0a4f96"/>
    <polygon points="605,0 856,177 430,177" fill="var(--white)"/>
  </svg>
  <div class="brand"><span class="brand-dot"></span><span class="brand-name">Brightlane Funding, Inc.</span></div>

  <div class="hero-photo" role="img" aria-label="Photo of a businesswoman and a contractor in a hard hat reviewing a clipboard in a bright renovated kitchen, with sketched plants and a ladder"></div>

  <h1 class="headline"><span class="line-one">HARD MONEY FIX &amp;</span><span class="line-two">FLIP PROGRAMS</span></h1>

  <p class="about">Brightlane Funding, Inc. was established in August 1997 by Marcus Welton. Over the years we have grown from a basement operated “one man show” to a staff of over 70 just before the real estate decline which started in 2007.</p>

  <div class="gallery">
    <div class="gallery-photo before" role="img" aria-label="Kitchen before renovation with light oak cabinets"></div>
    <div class="gallery-photo after" role="img" aria-label="Kitchen after renovation with dark wood cabinets and pendant lights"></div>
    <span class="gallery-label before">BEFORE</span>
    <span class="gallery-label after">AFTER</span>
  </div>

  <section class="programs">
    <h2 class="programs-title">WE OFFER A VARIETY OF<br><span>LOAN PROGRAMS</span></h2>
    <ul class="program-list">
      <li class="program-item" style="top:0">
        <svg class="program-icon" viewBox="0 0 38 38" aria-hidden="true"><circle cx="19" cy="19" r="18" fill="var(--gold)"/><circle cx="19" cy="19" r="14" fill="none" stroke="#2e2e30" stroke-width="1.5"/><rect x="11" y="13" width="14" height="10" fill="none" stroke="#2e2e30" stroke-width="1.8"/><circle cx="24" cy="22" r="3.5" fill="var(--gold)" stroke="#2e2e30" stroke-width="1.8"/><line x1="26.5" y1="24.5" x2="29" y2="27" stroke="#2e2e30" stroke-width="2"/></svg>
        No Minimum Credit Score</li>
      <li class="program-item" style="top:50px">
        <svg class="program-icon" viewBox="0 0 38 38" aria-hidden="true"><circle cx="19" cy="19" r="18" fill="var(--gold)"/><circle cx="19" cy="19" r="14" fill="none" stroke="#2e2e30" stroke-width="1.5"/><rect x="11" y="12" width="16" height="15" fill="none" stroke="#2e2e30" stroke-width="1.8"/><line x1="11" y1="16" x2="27" y2="16" stroke="#2e2e30" stroke-width="1.8"/><text x="19" y="25" font-size="8" font-weight="700" text-anchor="middle" fill="#2e2e30" font-family="Roboto,sans-serif">24</text></svg>
        3-5 Day Close</li>
      <li class="program-item" style="top:100px">
        <svg class="program-icon" viewBox="0 0 38 38" aria-hidden="true"><circle cx="19" cy="19" r="18" fill="var(--gold)"/><circle cx="19" cy="19" r="14" fill="none" stroke="#2e2e30" stroke-width="1.5"/><ellipse cx="19" cy="14" rx="6" ry="2.5" fill="#2e2e30"/><ellipse cx="19" cy="19" rx="6" ry="2.5" fill="#2e2e30"/><ellipse cx="19" cy="24" rx="6" ry="2.5" fill="#2e2e30"/></svg>
        Up to 100% of Purchase<br>&amp; Rehab</li>
      <li class="program-item" style="top:170px">
        <svg class="program-icon" viewBox="0 0 38 38" aria-hidden="true"><circle cx="19" cy="19" r="18" fill="var(--gold)"/><circle cx="19" cy="19" r="14" fill="none" stroke="#2e2e30" stroke-width="1.5"/><path d="M10 13h3l3 9h10l2-6H14" fill="none" stroke="#2e2e30" stroke-width="1.8"/><circle cx="17" cy="25" r="1.6" fill="#2e2e30"/><circle cx="24" cy="25" r="1.6" fill="#2e2e30"/></svg>
        Rates as Low as 7%</li>
      <li class="program-item" style="top:220px">
        <svg class="program-icon" viewBox="0 0 38 38" aria-hidden="true"><circle cx="19" cy="19" r="18" fill="var(--gold)"/><circle cx="19" cy="19" r="14" fill="none" stroke="#2e2e30" stroke-width="1.5"/><path d="M11 19l8-7 8 7M13 18v8h12v-8" fill="none" stroke="#2e2e30" stroke-width="1.8"/><rect x="17" y="21" width="4" height="5" fill="#2e2e30"/></svg>
        Loans Offered Nationwide</li>
    </ul>
  </section>

  <footer class="footer">
    Contact us today for more information at <span class="phone">(800) 647-2915 x42</span> or<br>
    email us at <em>mwelton@brightlanefunding.example</em> NMLS #731856 <em>www.brightlanefunding.example</em>
  </footer>
</div>
</body>
</html>
```